Business Card Design

We have recently seen two business cards that caught our attention and think the designs would work for us. We are an accounting firm that serves small businesses in a variety of industries. Attached are the two business card that inspired us along with very rough layouts. We would like to see a professional layout using our company information.

Industry/Entity Type

Accounting

Contact Information for Business Card

Company Name - Dalworth Pryce
Address - 4180 Brambleton Lane, Suite 310, Houston, TX 77051
713-508-9627 - Main
281-369-0714 - Fax

Team Member Names, emails and phone numbers (see attachment)

```html
<!DOCTYPE html>
<html lang="en">
<head>
<meta charset="utf-8">
<title>Dalworth Pryce – Business Card</title>
<link rel="stylesheet" href="https://fonts.googleapis.com/css2?family=Noto+Sans:wght@400;600&display=swap">
<style>
  :root {
    --backdrop: #b5b4b5;
    --card: #f4f4f4;
    --card-tone: #ececec;
    --ink: #111111;
    --muted: #a8a8a8;
    --frame: #141414;
  }
  * { box-sizing: border-box; margin: 0; padding: 0; }
  html, body {
    width: 1200px; height: 900px; overflow: hidden;
    background: var(--backdrop);
    font-family: "Noto Sans", sans-serif;
    color: var(--ink);
  }
  .card {
    position: absolute; left: 378px; top: 18px;
    width: 470px; height: 802px;
    background: var(--card);
  }
  .card__texture {
    position: absolute; inset: 0;
    background: linear-gradient(180deg, var(--card) 0%, var(--card-tone) 100%);
  }
  .card__frame {
    position: absolute; left: 6px; top: 8px; right: 9px; bottom: 9px;
    border: 7px solid var(--frame);
  }
  .brand {
    position: absolute; left: 0; right: 0; top: 182px;
    display: flex; flex-direction: column; align-items: center;
  }
  .brand__mark {
    width: 96px; height: 96px;
    background: var(--ink);
    margin-bottom: 70px;
  }
  .brand__name {
    font-size: 33px; font-weight: 400;
    letter-spacing: 3px; text-transform: uppercase;
    color: var(--ink);
  }
  .person {
    position: absolute; left: 36px; top: 546px;
  }
  .person__name { font-size: 25px; font-weight: 600; line-height: 1.2; }
  .person__title { font-size: 18px; color: var(--muted); line-height: 1.3; }
  .contact {
    position: absolute; left: 38px; top: 628px;
    font-size: 19.5px; line-height: 26px;
  }
  .contact__grid {
    display: grid; grid-template-columns: 76px auto;
  }
  .contact__grid dd { margin: 0; }
</style>
</head>
<body>
  <div class="card">
    <div class="card__texture" role="img" aria-label="Subtle light grey diamond pattern background"></div>
    <div class="card__frame"></div>

    <div class="brand">
      <div class="brand__mark"></div>
      <div class="brand__name">Dalworth Pryce</div>
    </div>

    <div class="person">
      <div class="person__name">Marisol Weaver</div>
      <div class="person__title">Account Manager</div>
    </div>

    <div class="contact">
      <dl class="contact__grid">
        <dt>Direct:</dt><dd>713-615-2048</dd>
        <dt>Mobile:</dt><dd>832-477-3951</dd>
        <dt>Main:</dt><dd>713-508-9627</dd>
        <dt>Fax:</dt><dd>281-369-0714</dd>
      </dl>
      <address style="font-style: normal;">
        4180 Brambleton Lane, Suite 310<br>
        Houston, TX 77051
      </address>
    </div>
  </div>
</body>
</html>
```